Graphic Design Needed for Powerpoint Deck

We need a powerpoint design template, font, and look and feel for a new company called Brookvale Care. Specific needs are listed in the attached file and if we like what we see we will more than likely use you in the future.
We like warm natural colors from a branding point of view, greens, browns, etc.
Target Market(s)
This will be used with potential investors and business partners.
Industry/Entity Type
Graphic Design
Requirements
Must have
- Graphic Designs for the charts mentioned in the powerpoint
- Overall Look and Feel
Nice to have
- Custom Font recommendations (Trebuchet is the one we like the most that is standard)

```html
<!DOCTYPE html>
<html lang="en">
<head>
<meta charset="utf-8">
<title>Brookvale Care – Solution</title>
<link href="https://fonts.googleapis.com/css2?family=Oswald:wght@300;400;500&family=Open+Sans:wght@400;600&display=swap" rel="stylesheet">
<style>
  :root{
    --bg:#efeeeb;
    --band:#f4f3f1;
    --ink:#3c3c3c;
    --ring:#3d3d3d;
    --hub:#e2e1de;
    --hub-arrow:#cfcecb;
    --accent:#e0782a;
    --cell-grey:#bcbcbc;
    --cell-white:#ffffff;
    --title-bar:#3a3a3a;
  }
  html,body{margin:0;padding:0;overflow:hidden;}
  body{width:1200px;height:900px;background:var(--bg);position:relative;font-family:"Open Sans",Arial,sans-serif;}
  .slide{position:absolute;inset:0;width:1200px;height:900px;overflow:hidden;}
  .cycle{position:absolute;left:0;top:0;width:1200px;height:700px;}
  .ring-label{font-family:"Oswald",Arial,sans-serif;font-weight:300;font-size:27px;fill:#fff;letter-spacing:0.5px;}
  .hub-title{font-family:"Oswald",Arial,sans-serif;font-weight:500;font-size:40px;fill:#2e2e2e;}
  .summary-band{position:absolute;left:0;top:706px;width:1200px;height:194px;background:var(--band);}
  .chevron{position:absolute;left:30px;top:716px;width:46px;height:134px;}
  .summary{position:absolute;left:130px;top:730px;width:530px;margin:0;font-size:21px;line-height:37px;color:#222;}
  .cost-table{position:absolute;left:687px;top:720px;width:505px;border-collapse:separate;border-spacing:2px;font-size:11.5px;color:#333;}
  .cost-table caption{background:var(--title-bar);color:#fff;font-weight:600;font-size:12px;padding:3px 0;margin-bottom:2px;}
  .cost-table th,.cost-table td{text-align:center;padding:0 2px;height:30px;}
  .cost-table thead th{background:var(--cell-grey);font-weight:400;line-height:1.1;}
  .cost-table thead th.blank{background:transparent;}
  .cost-table tbody th{background:var(--cell-grey);font-weight:400;width:92px;}
  .cost-table tbody td{background:var(--cell-white);}
  .cost-table .plan{background:var(--accent) !important;color:#fff;font-weight:600;}
</style>
</head>
<body>
<main class="slide">
  <svg class="cycle" viewBox="0 0 1200 700" aria-label="Four-part wellness cycle">
    <defs>
      <path id="arc-top" d="M487.2,234.5 A158 158 0 0 1 702.8,234.5"/>
      <path id="arc-right" d="M710.5,242.2 A158 158 0 0 1 710.5,457.8"/>
      <path id="arc-bottom" d="M468.8,485.2 A185 185 0 0 0 721.2,485.2"/>
      <path id="arc-left" d="M479.5,457.8 A158 158 0 0 1 479.5,242.2"/>
      <g id="segment">
        <path d="M458.6,203.7 A200 200 0 0 1 731.4,203.7 L691.8,246.2 A142 142 0 0 0 498.2,246.2 Z"/>
        <polygon points="571,152 619,152 595,122"/>
      </g>
    </defs>

    <g class="ring" fill="var(--ring)">
      <use href="#segment"/>
      <use href="#segment" transform="rotate(90 595 350)"/>
      <use href="#segment" transform="rotate(180 595 350)"/>
      <use href="#segment" transform="rotate(270 595 350)"/>
    </g>

    <text class="ring-label"><textPath href="#arc-top" startOffset="50%" text-anchor="middle">LIFESTYLE</textPath></text>
    <text class="ring-label"><textPath href="#arc-right" startOffset="50%" text-anchor="middle">PHYSICAL HEALTH</textPath></text>
    <text class="ring-label"><textPath href="#arc-bottom" startOffset="50%" text-anchor="middle">CLINICAL HEALTH</textPath></text>
    <text class="ring-label"><textPath href="#arc-left" startOffset="50%" text-anchor="middle">DIET</textPath></text>

    <g class="hub">
      <circle cx="595" cy="350" r="132" fill="var(--hub)"/>
      <path d="M510,330 A88 88 0 0 1 660,292" fill="none" stroke="var(--hub-arrow)" stroke-width="22"/>
      <polygon points="645,272 690,282 662,318" fill="var(--hub-arrow)"/>
      <path d="M680,370 A88 88 0 0 1 530,408" fill="none" stroke="var(--hub-arrow)" stroke-width="22"/>
      <polygon points="545,428 500,418 528,382" fill="var(--hub-arrow)"/>
      <text class="hub-title" x="595" y="364" text-anchor="middle">SOLUTION</text>
    </g>

    <g class="badges" fill="var(--accent)">
      <circle cx="595" cy="70" r="48" role="img" aria-label="Lifestyle icon: drink and person"/>
      <circle cx="880" cy="350" r="48" role="img" aria-label="Physical health icon: person with weights"/>
      <circle cx="595" cy="635" r="48" role="img" aria-label="Clinical health icon: hospital building"/>
      <circle cx="305" cy="350" r="48" role="img" aria-label="Diet icon: basket of fruit and vegetables"/>
    </g>
  </svg>

  <div class="summary-band"></div>
  <svg class="chevron" viewBox="0 0 46 134" aria-hidden="true">
    <polygon points="0,0 22,0 46,67 22,134 0,134 24,67" fill="var(--ink)"/>
  </svg>
  <p class="summary">Brookvale Care will provide the highest quality in holistic wellness including general preventative health, chiropractic, fitness, nutrition, massage therapy, and lifestyle coaching.</p>

  <table class="cost-table">
    <caption>Average California Health Costs</caption>
    <thead>
      <tr>
        <th class="blank"></th>
        <th>Employee</th>
        <th>Employer</th>
        <th>Total<br>insurance</th>
        <th class="plan">Brookvale<br>Holistic Gold</th>
      </tr>
    </thead>
    <tbody>
      <tr><th>Single</th><td>$974</td><td>$4,281</td><td>$5,255</td><td class="plan">$2400</td></tr>
      <tr><th>Couple</th><td>$2,961</td><td>$7,999</td><td>$10,960</td><td class="plan">$4800</td></tr>
      <tr><th>Family</th><td>$3,970</td><td>$11,867</td><td>$15,837</td><td class="plan">$6000</td></tr>
    </tbody>
  </table>
</main>
</body>
</html>
```